Bluegate Wound Care and Hyperbarics Website Refresh

I want to revamp my current website to be more streamlined and look cleaner. I am also adding additional service lines and another location to the company so I would like that added as well. I want to stick with the same logo and colors, but just have it cleaned up with a better overall design.

www.bghyperbarics-example.com

Target Market(s)

Wound Care and Hyperbaric Patients

Industry/Entity Type

Healthcare

Coding

Coded - Design and coding required

Number of Pages Required

5+ page

Colors
0054AA
0677BA
7BADD7
CADEEF
E8F1F8
59FF00
82FF00
B8FF75
E3FFCB
F4FFEA

```html
<!DOCTYPE html>
<html lang="en">
<head>
<meta charset="utf-8">
<title>Bluegate Wound Care &amp; Hyperbarics</title>
<link href="https://fonts.googleapis.com/css2?family=Poppins:wght@300;400;500;600&display=swap" rel="stylesheet">
<style>
:root{
  --navy:#0054AA; --blue:#0677BA; --sky:#7BADD7; --mist:#E8F1F8;
  --lime:#59FF00; --leaf:#82FF00; --ink:#2b2b2b; --foot:#1f1f1f;
}
*{box-sizing:border-box;margin:0;padding:0}
html,body{width:1200px;height:3626px;overflow:hidden;background:#fff}
body{font-family:'Poppins',sans-serif;color:var(--ink);position:relative}
.abs{position:absolute}
.topbar{left:0;top:0;width:1200px;height:30px;background:var(--navy);color:#fff;font-size:9px}
.topbar .item{position:absolute;top:0;height:30px;display:flex;align-items:center;gap:6px;white-space:nowrap}
.topbar svg{width:9px;height:9px}
.nav{left:0;top:30px;width:1200px;height:85px;background:#fff;border-bottom:1px solid #eee}
.brand{position:absolute;left:233px;top:26px;display:flex;align-items:center;gap:8px;font-size:26px;font-weight:500;color:var(--navy);letter-spacing:1px;line-height:32px}
.brand i{width:18px;height:18px;border-radius:50%;background:var(--blue);display:block}
.menu a{position:absolute;top:36px;font-size:9px;color:#444;text-decoration:none}
.menu a.on{color:var(--blue);font-weight:500}
.menu .sep{position:absolute;top:35px;width:1px;height:12px;background:#ddd}
.cta{position:absolute;left:865px;top:25px;width:104px;height:37px;border-radius:19px;background:#2b2b2b;color:#fff;font-size:8.5px;font-weight:600;display:flex;align-items:center;justify-content:center}
.hero{left:0;top:115px;width:1200px;height:524px;background:linear-gradient(135deg,#4f4843 0%,#6f6a64 40%,#837d73 70%,#5e5953 100%)}
.hero .kicker{position:absolute;left:0;width:1200px;top:164px;text-align:center;color:#eee;font-size:11px;letter-spacing:4px}
.hero h1{position:absolute;left:0;width:1200px;top:186px;text-align:center;color:#fff;font-size:41px;font-weight:600;line-height:56px}
.card{color:#fff;text-align:center;padding:0 28px}
.card h3{font-size:15px;font-weight:500;line-height:1.3;margin-bottom:16px}
.card p{font-size:10px;line-height:2;font-weight:300}
.card .btn{margin-top:18px}
.card.accent{color:var(--navy)}
.card.accent p{font-weight:400}
.btn{display:inline-flex;align-items:center;justify-content:center;gap:5px;height:34px;width:110px;border-radius:17px;font-size:8px;font-weight:600;text-transform:uppercase;white-space:nowrap}
.btn.white{background:#fff;color:var(--blue)}
.btn.ghost{border:1px solid #fff;color:#fff}
.btn.dark{background:var(--navy);color:#fff}
.btn.lime{background:var(--lime);color:var(--navy)}
h2{font-size:23px;font-weight:500;line-height:30px}
.lead{font-size:9.5px;line-height:2.1;color:#555;font-weight:300}
.copy{font-size:9.5px;line-height:2.1;font-weight:300;color:#fff}
.band{left:0;width:1200px}
.news{border:1px solid #e3e3e3;background:#fff}
.news .img{height:151px}
.news h4{font-size:12.5px;font-weight:500;line-height:1.55;margin:22px 15px 12px}
.news p{font-size:8px;line-height:1.75;color:#777;margin:0 15px}
.news em{display:block;font-style:normal;font-size:7.5px;color:var(--blue);margin:16px 15px;font-weight:600}
.field{background:#fff;height:34px;font-size:9px;color:#999;padding:10px 12px}
.foot h5{font-size:9px;font-weight:600;color:#fff;letter-spacing:.5px}
.foot p{font-size:8px;color:#bbb;white-space:nowrap}
.dot{width:7px;height:7px;border-radius:50%;background:#ddd;display:inline-block}
</style>
</head>
<body>

<header class="abs topbar">
  <span class="item" style="left:278px"><svg viewBox="0 0 10 10"><rect x="1" y="2" width="8" height="6" fill="#fff"/></svg>info@bluegate-example.com</span>
  <span class="item" style="left:469px"><svg viewBox="0 0 10 10"><path d="M2 1l2 2-1 1.5a5 5 0 0 0 2.5 2.5L7 6l2 2-1.5 1.5C5 9 1 5 .5 2z" fill="#fff"/></svg>555-010-4821</span>
  <span class="item" style="left:653px"><svg viewBox="0 0 10 10"><rect x="1" y="3" width="8" height="5" fill="#fff"/><rect x="3" y="1" width="4" height="2" fill="#fff"/></svg>555-010-4822</span>
  <span class="item" style="left:842px;gap:10px"><i class="dot" style="width:5px;height:5px"></i><i class="dot" style="width:5px;height:5px"></i><i class="dot" style="width:5px;height:5px"></i><i class="dot" style="width:5px;height:5px"></i></span>
</header>

<nav class="abs nav">
  <div class="brand"><i></i>BLUEGATE</div>
  <div class="menu">
    <a class="on" style="left:537px">HOME</a>
    <span class="sep" style="left:590px"></span>
    <a style="left:612px">ABOUT</a>
    <span class="sep" style="left:672px"></span>
    <a style="left:696px">BLOG</a>
  </div>
  <div class="cta">CONTACT US</div>
</nav>

<section class="abs hero" role="img" aria-label="Photo of a treatment room with hyperbaric oxygen chambers and a patient">
  <div class="kicker">State of the Art Wound Care</div>
  <h1>HYPERBARIC OXYGEN THERAPY</h1>
</section>

<article class="abs card accent" style="left:233px;top:518px;width:244px;height:247px;background:var(--leaf);padding-top:24px">
  <h3>Hyperbaric Oxygen<br>Therapy</h3>
  <p>Lorem ipsum dolor sit amet, consectetur adipiscing elit. Ut elit tellus, luctus nec ullamcorper mattis, pulvinar dapibus leo.</p>
  <span class="btn white">Learn more ➜</span>
</article>
<article class="abs card" style="left:477px;top:501px;width:245px;height:279px;background:var(--navy);padding-top:48px">
  <h3>Wound Care</h3>
  <p>Lorem ipsum dolor sit amet, consectetur adipiscing elit. Ut elit tellus, luctus nec ullamcorper mattis, pulvinar dapibus leo.</p>
  <span class="btn ghost">Learn more ➜</span>
</article>
<article class="abs card" style="left:722px;top:518px;width:244px;height:247px;background:var(--blue);padding-top:24px">
  <h3>Your Multiple Service<br>Provider</h3>
  <p>At Bluegate, you will be treated by a highly-skilled provider, specially trained in wound care &amp; hyperbaric medicine.</p>
  <span class="btn white">Learn more ➜</span>
</article>

<h2 class="abs" style="left:233px;top:877px">Wound Care at Bluegate:</h2>
<span class="btn dark abs" style="left:233px;top:929px">Learn more ➜</span>
<p class="lead abs" style="left:632px;top:878px;width:336px">At Bluegate Wound Care &amp; Hyperbarics we are committed to the highest level of care with state of the art technology in our hyperbaric oxygen therapy clinic. Our stand-alone clinic offers hyperbaric medicine in a conveniently located, outpatient setting.</p>

<section class="abs band" style="top:1118px;height:369px;background:var(--navy)"></section>
<h2 class="abs" style="left:233px;top:1190px;color:#fff">Mission Statement</h2>
<p class="abs copy" style="left:233px;top:1244px;width:345px">Bluegate Wound Care &amp; Hyperbarics is dedicated to the highest level of service with state of the art science for wound care. We are committed to our patient's overall wellbeing and health. We always do what is right for the patient. We will not waiver in our standard of care for our valued customers.</p>
<span class="btn ghost abs" style="left:233px;top:1376px">Learn more ➜</span>
<div class="abs" role="img" aria-label="Photo of the clinic waiting room with blue chairs" style="left:630px;top:1067px;width:332px;height:420px;background:linear-gradient(180deg,#ece8e0 0%,#dcd5c8 55%,#b8b0a3 100%)"></div>

<section class="abs band" style="top:1487px;height:258px;background:var(--mist)"></section>
<h2 class="abs" style="left:233px;top:1583px">How We Heal?</h2>
<span class="btn lime abs" style="left:233px;top:1636px">Learn more ➜</span>
<p class="lead abs" style="left:632px;top:1588px;width:336px">Did you know that we all heal the same basic way? Our bodies are designed to close holes in the skin through very efficient and orderly processes.</p>

<section class="abs band" style="top:1745px;height:428px;background:var(--navy)"></section>
<div class="abs" role="img" aria-label="Group photo of the clinic care team" style="left:233px;top:1745px;width:331px;height:468px;background:linear-gradient(180deg,#c8c4bd 0%,#a59f95 55%,#7a6d5c 100%)"></div>
<h2 class="abs" style="left:621px;top:1806px;color:#fff">About Bluegate</h2>
<p class="abs copy" style="left:621px;top:1858px;width:345px">Realizing the need for the underutilization of hyperbaric oxygen therapy (HBOT) is why Bluegate Wound Care &amp; Hyperbarics was founded. Daniel understands many physicians want the opportunity to have HBOT as an option for their patients, but the risk of sending them to a major hospital system only to never see that patient again was unappealing.</p>
<div class="abs" style="left:621px;top:2005px;width:41px;height:41px;border-radius:50%;background:#e8e8e8"></div>
<p class="abs" style="left:674px;top:2012px;font-size:8.5px;font-weight:500;color:#fff">Daniel R. Moore</p>
<p class="abs" style="left:674px;top:2027px;font-size:7.5px;font-weight:300;color:#fff">CEO</p>
<span class="btn ghost abs" style="left:621px;top:2077px;width:100px">About us ➜</span>

<h2 class="abs" style="left:233px;top:2296px">Our Latest News</h2>
<p class="lead abs" style="left:632px;top:2300px;width:336px">Some dummy text snippet/filler as a text filler used for design purposes only, which will then be replaced.</p>

<article class="abs news" style="left:233px;top:2388px;width:231px;height:342px">
  <div class="img" role="img" aria-label="Photo of a clinician treating a patient's foot" style="background:linear-gradient(135deg,#e4eef0,#9fc0c3)"></div>
  <h4>3 Tips To Prevent Diabetic Ulcers: When To Consider Hyperbaric Therapy</h4>
  <p>People with diabetes are more prone to infected wounds and diabetic ulcers. Hyperbaric therapy can help these infections heal faster.</p>
  <em>READ MORE ›</em>
</article>
<article class="abs news" style="left:485px;top:2388px;width:231px;height:342px">
  <div class="img" role="img" aria-label="Photo of a patient inside a hyperbaric chamber" style="background:linear-gradient(135deg,#9aa1a6,#4e555c)"></div>
  <h4>Autism, Cerebral Palsy, Fibromyalgia: 3 Less-Known Reasons To Consider HBOT</h4>
  <p>Hyperbaric oxygen therapy (HBOT) provides pure oxygen in a pressurized chamber, improving conditions such as autism, cerebral palsy, and fibromyalgia.</p>
  <em>READ MORE ›</em>
</article>
<article class="abs news" style="left:735px;top:2388px;width:231px;height:342px">
  <div class="img" role="img" aria-label="Photo of a monoplace hyperbaric chamber" style="background:linear-gradient(135deg,#eef1f5,#9aa9c2)"></div>
  <h4>How Many HBOT Sessions Do I Need? Treatment for Common Conditions</h4>
  <p>HBOT continues to be an effective means of treating a range of common health issues. However, each condition needs several sessions to heal effectively.</p>
  <em>READ MORE ›</em>
</article>

<section class="abs band" role="img" aria-label="Photo of the clinic building under a blue tint" style="top:2805px;height:520px;background:linear-gradient(180deg,#1f6fb8,#0a5aa8)"></section>
<h2 class="abs" style="left:0;width:1200px;top:2876px;text-align:center;color:#fff">Contact Us Today</h2>
<p class="abs copy" style="left:352px;width:496px;top:2918px;text-align:center">Constantly looking for ways to evolve the treatment of wounds and provide services that add value to the providers who refer patients to our facilities.</p>
<div class="abs field" style="left:344px;top:2992px;width:246px">Name</div>
<div class="abs field" style="left:605px;top:2992px;width:247px">Email</div>
<div class="abs field" style="left:344px;top:3037px;width:246px">Phone</div>
<div class="abs field" style="left:605px;top:3037px;width:247px">Subject</div>
<div class="abs field" style="left:344px;top:3083px;width:508px;height:91px">Message</div>
<span class="btn lime abs" style="left:543px;top:3191px;width:114px;height:36px;border-radius:18px">Send message ➜</span>

<footer class="abs band foot" style="top:3325px;height:301px;background:var(--foot)">
  <h5 class="abs" style="left:233px;top:76px">LOCATIONS</h5>
  <p class="abs" style="left:233px;top:126px">⌖ &nbsp;1200 Example Pkwy, Suite 210, Springfield, TX 75000</p>
  <p class="abs" style="left:233px;top:152px">⌖ &nbsp;1200 Example Pkwy, Suite 210, Springfield, TX 75000</p>
  <h5 class="abs" style="left:575px;top:76px">QUICK LINKS</h5>
  <p class="abs" style="left:575px;top:126px">→ &nbsp;Home</p>
  <p class="abs" style="left:665px;top:126px">→ &nbsp;About</p>
  <p class="abs" style="left:575px;top:152px">→ &nbsp;Blog</p>
  <p class="abs" style="left:665px;top:152px">→ &nbsp;Contact</p>
  <h5 class="abs" style="left:886px;top:76px">FOLLOW US</h5>
  <div class="abs" style="left:892px;top:128px;display:flex;gap:12px"><i class="dot" style="width:6px;height:6px"></i><i class="dot" style="width:6px;height:6px"></i><i class="dot" style="width:6px;height:6px"></i><i class="dot" style="width:6px;height:6px"></i></div>
  <p class="abs" style="left:233px;top:218px">◷ &nbsp;Office Hours: Monday - Friday | 8:00am - 5:00pm</p>
  <p class="abs" style="right:234px;top:218px">© Copyright 2022 Bluegate - All Rights Reserved</p>
</footer>

</body>
</html>
```